"Oral Surgery Office needs a Business Card Design with Logo"

We need a logo design and business card. The name of the office is Tassingford Oral Surgery & Implant Center. The final design should communicate uniqueness as well as highly class office. The business card should emphasize power. I included the current business card below. Please design something unique

Target Market(s)

Dentists & Patients

Industry/Entity Type

Dental

Contact Information for Business Card

Unique Design to show success, prestige, Style, unmatched performance

Font styles to use
Serif

Colors
1b1b1b
ffffff
0556a4

Requirements
Must have
• Bussiness Name, Doctor's Name, Website, phone and Fax, email, office address
• Color should be either Black and White or Blue and White
Nice to have
• Clean look
Should not have
• the business card shouldn't be too busy. I feel like the old business card was too busy

```html
<!DOCTYPE html>
<html lang="en">
<head>
<meta charset="utf-8">
<title>Tassingford Oral Surgery &amp; Implant Center — Business Card</title>
<link href="https://fonts.googleapis.com/css2?family=Open+Sans:wght@400;600;700&display=swap" rel="stylesheet">
<style>
  :root {
    --stage: #000000;
    --card: #ffffff;
    --card-fade: #ececec;
    --navy: #16165e;
    --ink: #2b2b2b;
    --muted: #5d5d66;
    --rule: #a9a3cf;
    --ghost-a: #ececec;
    --ghost-b: #f8f8f8;
    --edge: #bdbdbd;
  }
  * { margin: 0; padding: 0; box-sizing: border-box; }
  html, body { width: 1200px; height: 900px; overflow: hidden; background: var(--stage); }
  body { position: relative; font-family: "Open Sans", Arial, sans-serif; color: var(--ink); }

  .card {
    position: absolute; top: 271px; width: 457px; height: 281px;
    border-radius: 14px; overflow: hidden; background: var(--card);
  }
  .card--front { left: 137px; }
  .card--back {
    left: 626px;
    background: linear-gradient(180deg, var(--card) 0%, var(--card-fade) 100%);
    box-shadow: 0 0 0 1px var(--edge);
  }

  .ghost-emblem {
    position: absolute; left: 275px; top: -10px; width: 180px; height: 130px;
    border-radius: 50%;
    background: radial-gradient(ellipse at center, var(--ghost-a) 0%, var(--ghost-b) 65%, rgba(255,255,255,0) 100%);
  }

  .wordmark {
    position: absolute; left: 25px; top: 26px;
    color: var(--navy); font-weight: 600; font-size: 20px; line-height: 23px;
    text-transform: uppercase; letter-spacing: 0.2px;
  }

  .divider { position: absolute; left: 0; top: 138px; width: 198px; height: 1px; background: var(--rule); }
  .accent-bar { position: absolute; right: 0; top: 117px; width: 9px; height: 136px; background: var(--navy); }

  .doctor { position: absolute; right: 25px; top: 129px; text-align: right; white-space: nowrap; }
  .doctor__name { color: var(--navy); font-weight: 700; font-size: 15px; line-height: 20px; }
  .doctor__title { color: var(--muted); font-size: 13.5px; line-height: 20px; }

  .contacts { position: absolute; right: 25px; top: 187px; list-style: none; }
  .contacts li {
    display: flex; justify-content: flex-end; align-items: center; white-space: nowrap;
    font-size: 12px; line-height: 16.5px; color: var(--ink);
  }
  .contacts svg { width: 10px; height: 10px; margin-left: 7px; fill: var(--navy); }

  .address { position: absolute; left: 25px; top: 220px; font-size: 12px; line-height: 16.5px; font-style: normal; white-space: nowrap; }

  .brand { position: absolute; left: 98px; top: 106px; display: flex; align-items: center; }
  .brand__mark { width: 64px; height: 64px; border-radius: 50%; background: var(--navy); margin-right: 16px; }
  .brand__name {
    color: var(--navy); font-weight: 600; font-size: 19px; line-height: 21px; text-transform: uppercase;
  }

  .socials { position: absolute; left: 50px; top: 225px; display: flex; gap: 18px; list-style: none; }
  .socials li { display: flex; align-items: center; font-size: 12px; line-height: 16px; color: var(--ink); white-space: nowrap; }
  .socials .dot { width: 13px; height: 13px; border-radius: 2px; background: var(--navy); margin-right: 4px; flex: none; }
</style>
</head>
<body>
  <section class="card card--front" aria-label="Business card front">
    <div class="ghost-emblem" role="img" aria-label="Faint practice emblem decoration"></div>
    <h1 class="wordmark">Tassingford<br>Oral Surgery &amp;<br>Implant Center</h1>
    <div class="divider"></div>
    <div class="doctor">
      <p class="doctor__name">DR. MORRIS VENHALDT, D.D.S</p>
      <p class="doctor__title">Oral &amp; Maxilofacial surgery</p>
    </div>
    <ul class="contacts">
      <li>555-014-2281<svg viewBox="0 0 10 10"><path d="M1 4c0-2 1-3 4-3s4 1 4 3H7V3H3v1zM2 5h6l1 4H1z"/></svg></li>
      <li>555-014-2296<svg viewBox="0 0 10 10"><path d="M2 1h6v3H2zM1 4h8v5H1zM3 6h4v2H3z"/></svg></li>
      <li>TassingfordOralSurgeon@mail.com<svg viewBox="0 0 10 10"><path d="M1 2h8v6H1zM1 2l4 3 4-3"/></svg></li>
      <li>www.TassingfordOralSurgery.com<svg viewBox="0 0 10 10"><circle cx="5" cy="5" r="4.5"/></svg></li>
    </ul>
    <address class="address">87 Harrow Lane<br>Tassingford, NY 10412</address>
    <div class="accent-bar"></div>
  </section>

  <section class="card card--back" aria-label="Business card back">
    <div class="brand">
      <span class="brand__mark"></span>
      <p class="brand__name">Tassingford<br>Oral Surgery &amp;<br>Implant Center</p>
    </div>
    <ul class="socials">
      <li><span class="dot"></span>TassOralSurgeon</li>
      <li><span class="dot"></span>Tassingford Oral Surgery &amp; implant Center</li>
    </ul>
  </section>
</body>
</html>
```